Team email banner for internal communications

We need a team email banner/header that will be applied to all internal communications from our department to other functions. The graphic should be optimized for Outlook and be landscape in layout. We have 5 different silo within our team and will need so will either need have a blank space to denote each team or have change in colors/graphics to denote each team (see current headers attached to job description). We are looking for a banner that combines our team logo (attached) with our team name, Commercial Learning & Development. The theme should be L&D and pharmaceutical in nature.

Need extra days to review

The text in the banner should be Commercial Learning & Development with the team logo (attached).

```html
<!DOCTYPE html>
<html lang="en">
<head>
<meta charset="utf-8">
<title>Team Email Banners</title>
<link href="https://fonts.googleapis.com/css2?family=Montserrat:ital,wght@0,700;1,800&display=swap" rel="stylesheet">
<style>
  :root {
    --page: #ffffff;
    --ink: #0b0b0b;
    --base: #f2f2f2;
    --dot: #dcdcdc;
    --blue: #1f80dc; --blue-deep: #1562b5; --blue-photo-a: #9cc4ee; --blue-photo-b: #2f6fc0;
    --red: #d8261c; --red-deep: #a31f1f; --red-photo-a: #f0463c; --red-photo-b: #a5141a;
    --purple: #6b2a7e; --purple-deep: #4b2257; --purple-photo-a: #9a52b5; --purple-photo-b: #4e1d63;
    --green: #16b086; --green-deep: #0e876a; --green-photo-a: #2a9a7e; --green-photo-b: #0d5a4b;
  }
  * { margin: 0; padding: 0; box-sizing: border-box; }
  html, body { width: 1200px; height: 578px; overflow: hidden; background: var(--page); }
  .canvas { position: relative; width: 1200px; height: 578px; font-family: "Montserrat", sans-serif; }

  .banner { position: absolute; width: 470px; height: 157px; overflow: hidden;
    background:
      repeating-linear-gradient(120deg, rgba(255,255,255,0) 0 40px, rgba(255,255,255,.55) 40px 70px, rgba(255,255,255,0) 70px 110px),
      var(--base); }
  .banner--leadership { left: 121px; top: 125px; --accent: var(--blue); --accent-deep: var(--blue-deep); }
  .banner--hematology { left: 610px; top: 125px; --accent: var(--red); --accent-deep: var(--red-deep); }
  .banner--tumor { left: 121px; top: 298px; --accent: var(--purple); --accent-deep: var(--purple-deep); }
  .banner--operations { left: 610px; top: 298px; --accent: var(--green); --accent-deep: var(--green-deep); }

  .banner__art { position: absolute; inset: 0; width: 470px; height: 157px; }
  .art-ink { fill: var(--ink); }
  .art-accent { fill: var(--accent); }
  .art-accent-deep { fill: var(--accent-deep); }
  .art-dot { fill: var(--dot); }

  .brand { position: absolute; left: 9px; top: 16px; display: flex; align-items: center; gap: 6px; }
  .brand__dot { width: 12px; height: 12px; border-radius: 50%; background: var(--ink); }
  .brand__name { font-weight: 700; font-size: 12.5px; color: var(--ink); letter-spacing: .2px; }

  .banner__title { position: absolute; left: 18px; top: 65px; font-weight: 800; font-style: italic;
    font-size: 19px; line-height: 24px; color: var(--accent); white-space: nowrap; }
</style>
</head>
<body>
<div class="canvas">

  <section class="banner banner--leadership">
    <svg class="banner__art" viewBox="0 0 470 157">
      <defs>
        <linearGradient id="photo-leadership" x1="0" y1="0" x2="1" y2="1">
          <stop offset="0" stop-color="var(--blue-photo-a)"/><stop offset="1" stop-color="var(--blue-photo-b)"/>
        </linearGradient>
      </defs>
      <rect class="art-ink" x="0" y="0" width="470" height="5"/>
      <g class="dot-grid">
        <circle class="art-dot" cx="237" cy="15" r="2.4"/><circle class="art-dot" cx="247" cy="15" r="2.4"/><circle class="art-dot" cx="257" cy="15" r="2.4"/><circle class="art-dot" cx="267" cy="15" r="2.4"/><circle class="art-dot" cx="277" cy="15" r="2.4"/><circle class="art-dot" cx="287" cy="15" r="2.4"/><circle class="art-dot" cx="297" cy="15" r="2.4"/><circle class="art-dot" cx="307" cy="15" r="2.4"/><circle class="art-dot" cx="317" cy="15" r="2.4"/>
        <circle class="art-dot" cx="237" cy="25.5" r="2.4"/><circle class="art-dot" cx="247" cy="25.5" r="2.4"/><circle class="art-dot" cx="257" cy="25.5" r="2.4"/><circle class="art-dot" cx="267" cy="25.5" r="2.4"/><circle class="art-dot" cx="277" cy="25.5" r="2.4"/><circle class="art-dot" cx="287" cy="25.5" r="2.4"/><circle class="art-dot" cx="297" cy="25.5" r="2.4"/><circle class="art-dot" cx="307" cy="25.5" r="2.4"/><circle class="art-dot" cx="317" cy="25.5" r="2.4"/>
        <circle class="art-dot" cx="237" cy="36" r="2.4"/><circle class="art-dot" cx="247" cy="36" r="2.4"/><circle class="art-dot" cx="257" cy="36" r="2.4"/><circle class="art-dot" cx="267" cy="36" r="2.4"/><circle class="art-dot" cx="277" cy="36" r="2.4"/><circle class="art-dot" cx="287" cy="36" r="2.4"/><circle class="art-dot" cx="297" cy="36" r="2.4"/><circle class="art-dot" cx="307" cy="36" r="2.4"/><circle class="art-dot" cx="317" cy="36" r="2.4"/>
        <circle class="art-dot" cx="237" cy="46.5" r="2.4"/><circle class="art-dot" cx="247" cy="46.5" r="2.4"/><circle class="art-dot" cx="257" cy="46.5" r="2.4"/><circle class="art-dot" cx="267" cy="46.5" r="2.4"/><circle class="art-dot" cx="277" cy="46.5" r="2.4"/><circle class="art-dot" cx="287" cy="46.5" r="2.4"/><circle class="art-dot" cx="297" cy="46.5" r="2.4"/><circle class="art-dot" cx="307" cy="46.5" r="2.4"/><circle class="art-dot" cx="317" cy="46.5" r="2.4"/>
      </g>
      <polygon class="art-ink" points="0,157 201,134 420,90 420,157"/>
      <polygon class="art-accent" points="201,134 420,68 420,157 150,157"/>
      <polygon class="art-accent-deep" points="133,157 317,122 420,110 420,157"/>
      <path class="art-ink" d="M400,-14 A94,92 0 0 0 400,170 L470,170 L470,-14 Z"/>
      <path role="img" aria-label="Photo of colleagues stacking hands together in teamwork, blue tint" fill="url(#photo-leadership)" d="M404,-8 A86,86 0 0 0 404,164 L470,164 L470,-8 Z"/>
    </svg>
    <div class="brand"><span class="brand__dot"></span><span class="brand__name">Meridian Learning</span></div>
    <h2 class="banner__title">Leadership Developtment</h2>
  </section>

  <section class="banner banner--hematology">
    <svg class="banner__art" viewBox="0 0 470 157">
      <defs>
        <radialGradient id="photo-hematology" cx=".4" cy=".35" r=".8">
          <stop offset="0" stop-color="var(--red-photo-a)"/><stop offset="1" stop-color="var(--red-photo-b)"/>
        </radialGradient>
      </defs>
      <rect class="art-ink" x="0" y="0" width="470" height="5"/>
      <g class="dot-grid">
        <circle class="art-dot" cx="237" cy="15" r="2.4"/><circle class="art-dot" cx="247" cy="15" r="2.4"/><circle class="art-dot" cx="257" cy="15" r="2.4"/><circle class="art-dot" cx="267" cy="15" r="2.4"/><circle class="art-dot" cx="277" cy="15" r="2.4"/><circle class="art-dot" cx="287" cy="15" r="2.4"/><circle class="art-dot" cx="297" cy="15" r="2.4"/><circle class="art-dot" cx="307" cy="15" r="2.4"/><circle class="art-dot" cx="317" cy="15" r="2.4"/>
        <circle class="art-dot" cx="237" cy="25.5" r="2.4"/><circle class="art-dot" cx="247" cy="25.5" r="2.4"/><circle class="art-dot" cx="257" cy="25.5" r="2.4"/><circle class="art-dot" cx="267" cy="25.5" r="2.4"/><circle class="art-dot" cx="277" cy="25.5" r="2.4"/><circle class="art-dot" cx="287" cy="25.5" r="2.4"/><circle class="art-dot" cx="297" cy="25.5" r="2.4"/><circle class="art-dot" cx="307" cy="25.5" r="2.4"/><circle class="art-dot" cx="317" cy="25.5" r="2.4"/>
        <circle class="art-dot" cx="237" cy="36" r="2.4"/><circle class="art-dot" cx="247" cy="36" r="2.4"/><circle class="art-dot" cx="257" cy="36" r="2.4"/><circle class="art-dot" cx="267" cy="36" r="2.4"/><circle class="art-dot" cx="277" cy="36" r="2.4"/><circle class="art-dot" cx="287" cy="36" r="2.4"/><circle class="art-dot" cx="297" cy="36" r="2.4"/><circle class="art-dot" cx="307" cy="36" r="2.4"/><circle class="art-dot" cx="317" cy="36" r="2.4"/>
        <circle class="art-dot" cx="237" cy="46.5" r="2.4"/><circle class="art-dot" cx="247" cy="46.5" r="2.4"/><circle class="art-dot" cx="257" cy="46.5" r="2.4"/><circle class="art-dot" cx="267" cy="46.5" r="2.4"/><circle class="art-dot" cx="277" cy="46.5" r="2.4"/><circle class="art-dot" cx="287" cy="46.5" r="2.4"/><circle class="art-dot" cx="297" cy="46.5" r="2.4"/><circle class="art-dot" cx="307" cy="46.5" r="2.4"/><circle class="art-dot" cx="317" cy="46.5" r="2.4"/>
      </g>
      <polygon class="art-ink" points="0,157 201,134 420,90 420,157"/>
      <polygon class="art-accent" points="201,134 420,68 420,157 150,157"/>
      <polygon class="art-accent-deep" points="133,157 317,122 420,110 420,157"/>
      <path class="art-ink" d="M400,-14 A94,92 0 0 0 400,170 L470,170 L470,-14 Z"/>
      <path role="img" aria-label="Close-up image of red blood cells" fill="url(#photo-hematology)" d="M404,-8 A86,86 0 0 0 404,164 L470,164 L470,-8 Z"/>
    </svg>
    <div class="brand"><span class="brand__dot"></span><span class="brand__name">Meridian Learning</span></div>
    <h2 class="banner__title">Herematology</h2>
  </section>

  <section class="banner banner--tumor">
    <svg class="banner__art" viewBox="0 0 470 157">
      <defs>
        <linearGradient id="photo-tumor" x1="0" y1="0" x2="1" y2="1">
          <stop offset="0" stop-color="var(--purple-photo-a)"/><stop offset="1" stop-color="var(--purple-photo-b)"/>
        </linearGradient>
      </defs>
      <rect class="art-ink" x="0" y="0" width="470" height="5"/>
      <g class="dot-grid">
        <circle class="art-dot" cx="237" cy="15" r="2.4"/><circle class="art-dot" cx="247" cy="15" r="2.4"/><circle class="art-dot" cx="257" cy="15" r="2.4"/><circle class="art-dot" cx="267" cy="15" r="2.4"/><circle class="art-dot" cx="277" cy="15" r="2.4"/><circle class="art-dot" cx="287" cy="15" r="2.4"/><circle class="art-dot" cx="297" cy="15" r="2.4"/><circle class="art-dot" cx="307" cy="15" r="2.4"/><circle class="art-dot" cx="317" cy="15" r="2.4"/>
        <circle class="art-dot" cx="237" cy="25.5" r="2.4"/><circle class="art-dot" cx="247" cy="25.5" r="2.4"/><circle class="art-dot" cx="257" cy="25.5" r="2.4"/><circle class="art-dot" cx="267" cy="25.5" r="2.4"/><circle class="art-dot" cx="277" cy="25.5" r="2.4"/><circle class="art-dot" cx="287" cy="25.5" r="2.4"/><circle class="art-dot" cx="297" cy="25.5" r="2.4"/><circle class="art-dot" cx="307" cy="25.5" r="2.4"/><circle class="art-dot" cx="317" cy="25.5" r="2.4"/>
        <circle class="art-dot" cx="237" cy="36" r="2.4"/><circle class="art-dot" cx="247" cy="36" r="2.4"/><circle class="art-dot" cx="257" cy="36" r="2.4"/><circle class="art-dot" cx="267" cy="36" r="2.4"/><circle class="art-dot" cx="277" cy="36" r="2.4"/><circle class="art-dot" cx="287" cy="36" r="2.4"/><circle class="art-dot" cx="297" cy="36" r="2.4"/><circle class="art-dot" cx="307" cy="36" r="2.4"/><circle class="art-dot" cx="317" cy="36" r="2.4"/>
        <circle class="art-dot" cx="237" cy="46.5" r="2.4"/><circle class="art-dot" cx="247" cy="46.5" r="2.4"/><circle class="art-dot" cx="257" cy="46.5" r="2.4"/><circle class="art-dot" cx="267" cy="46.5" r="2.4"/><circle class="art-dot" cx="277" cy="46.5" r="2.4"/><circle class="art-dot" cx="287" cy="46.5" r="2.4"/><circle class="art-dot" cx="297" cy="46.5" r="2.4"/><circle class="art-dot" cx="307" cy="46.5" r="2.4"/><circle class="art-dot" cx="317" cy="46.5" r="2.4"/>
      </g>
      <polygon class="art-ink" points="0,157 201,134 420,90 420,157"/>
      <polygon class="art-accent" points="201,134 420,68 420,157 150,157"/>
      <polygon class="art-accent-deep" points="133,157 317,122 420,110 420,157"/>
      <path class="art-ink" d="M400,-14 A94,92 0 0 0 400,170 L470,170 L470,-14 Z"/>
      <path role="img" aria-label="Microscopic image of porous tumor tissue, purple tint" fill="url(#photo-tumor)" d="M404,-8 A86,86 0 0 0 404,164 L470,164 L470,-8 Z"/>
    </svg>
    <div class="brand"><span class="brand__dot"></span><span class="brand__name">Meridian Learning</span></div>
    <h2 class="banner__title">Solid Tumor</h2>
  </section>

  <section class="banner banner--operations">
    <svg class="banner__art" viewBox="0 0 470 157">
      <defs>
        <linearGradient id="photo-operations" x1="0" y1="0" x2="1" y2="1">
          <stop offset="0" stop-color="var(--green-photo-a)"/><stop offset="1" stop-color="var(--green-photo-b)"/>
        </linearGradient>
      </defs>
      <rect class="art-ink" x="0" y="0" width="470" height="5"/>
      <g class="dot-grid">
        <circle class="art-dot" cx="237" cy="15" r="2.4"/><circle class="art-dot" cx="247" cy="15" r="2.4"/><circle class="art-dot" cx="257" cy="15" r="2.4"/><circle class="art-dot" cx="267" cy="15" r="2.4"/><circle class="art-dot" cx="277" cy="15" r="2.4"/><circle class="art-dot" cx="287" cy="15" r="2.4"/><circle class="art-dot" cx="297" cy="15" r="2.4"/><circle class="art-dot" cx="307" cy="15" r="2.4"/><circle class="art-dot" cx="317" cy="15" r="2.4"/>
        <circle class="art-dot" cx="237" cy="25.5" r="2.4"/><circle class="art-dot" cx="247" cy="25.5" r="2.4"/><circle class="art-dot" cx="257" cy="25.5" r="2.4"/><circle class="art-dot" cx="267" cy="25.5" r="2.4"/><circle class="art-dot" cx="277" cy="25.5" r="2.4"/><circle class="art-dot" cx="287" cy="25.5" r="2.4"/><circle class="art-dot" cx="297" cy="25.5" r="2.4"/><circle class="art-dot" cx="307" cy="25.5" r="2.4"/><circle class="art-dot" cx="317" cy="25.5" r="2.4"/>
        <circle class="art-dot" cx="237" cy="36" r="2.4"/><circle class="art-dot" cx="247" cy="36" r="2.4"/><circle class="art-dot" cx="257" cy="36" r="2.4"/><circle class="art-dot" cx="267" cy="36" r="2.4"/><circle class="art-dot" cx="277" cy="36" r="2.4"/><circle class="art-dot" cx="287" cy="36" r="2.4"/><circle class="art-dot" cx="297" cy="36" r="2.4"/><circle class="art-dot" cx="307" cy="36" r="2.4"/><circle class="art-dot" cx="317" cy="36" r="2.4"/>
        <circle class="art-dot" cx="237" cy="46.5" r="2.4"/><circle class="art-dot" cx="247" cy="46.5" r="2.4"/><circle class="art-dot" cx="257" cy="46.5" r="2.4"/><circle class="art-dot" cx="267" cy="46.5" r="2.4"/><circle class="art-dot" cx="277" cy="46.5" r="2.4"/><circle class="art-dot" cx="287" cy="46.5" r="2.4"/><circle class="art-dot" cx="297" cy="46.5" r="2.4"/><circle class="art-dot" cx="307" cy="46.5" r="2.4"/><circle class="art-dot" cx="317" cy="46.5" r="2.4"/>
      </g>
      <polygon class="art-ink" points="0,157 201,134 420,90 420,157"/>
      <polygon class="art-accent" points="201,134 420,68 420,157 150,157"/>
      <polygon class="art-accent-deep" points="133,157 317,122 420,110 420,157"/>
      <path class="art-ink" d="M400,-14 A94,92 0 0 0 400,170 L470,170 L470,-14 Z"/>
      <path role="img" aria-label="Photo of a surgical team at work in an operating room, green tint" fill="url(#photo-operations)" d="M404,-8 A86,86 0 0 0 404,164 L470,164 L470,-8 Z"/>
    </svg>
    <div class="brand"><span class="brand__dot"></span><span class="brand__name">Meridian Learning</span></div>
    <h2 class="banner__title">Operations &amp; Capabilities</h2>
  </section>

</div>
</body>
</html>
```